Dental Practice Billboard Design

We are a newer dental practice in need of a simple but appealing billboard for our growing dental practice to attract new patients. The practice is owned by husband and wife dentists and is family friendly in a small town in Kentucky. We try to be very friendly and caring to our patients. Would prefer a blue background for the billboard and our tooth logo to be prominent. We are partial to the Patua One font used in the image below but please feel free to tweak it as you deem necessary. The shape of the uppercase D and lowercase g are why we like that font, so fonts with a similarly shaped “D” and “g” would work as well. Please include our phone number (606) 847-3962. Please see our website Harlowfamilydentistry.com for more info on the practice if needed. Thank you! Looking forward to seeing your creation.
Updates

The dimensions will be 12ft x 24ft (3.6576m x 7.3152m). Apologies for not including this in the original prompt. Thank you all for your submissions.

Industry/Entity Type

Dental

Font styles to use
Other font styles liked:
• Patua One

Colors
0054AA
0677BA
7BADD7
CADEEF
E8F1F8
0094D4
00A9DD
6FCCEA
C7EBF8
E9F6FB
00AB8E
00BBA5
67D7C9
C6EFE9
E9F9F6
59FF00
82FF00
B8FF75
E3FFCB
F4FFEA

Requirements
Must have
• Phone number, website, Logo, Practice name “Harlow Family Dentistry”
Should not have
• A tagline or slogan

```html
<!DOCTYPE html>
<html lang="en">
<head>
<meta charset="utf-8">
<title>Harlow Family Dentistry Billboard</title>
<link rel="stylesheet" href="https://fonts.googleapis.com/css2?family=Patua+One&display=swap">
<style>
  :root {
    --navy-deep: #0a2157;
    --navy: #0b3585;
    --royal: #0054AA;
    --sky-wave: #3d6fc0;
    --band-blue: #0a5cc4;
    --green: #17b21a;
    --white: #ffffff;
    --stage: #e8f1f8;
  }
  html, body {
    margin: 0;
    padding: 0;
    width: 1200px;
    height: 858px;
    overflow: hidden;
    background: var(--stage);
  }
  .billboard {
    position: absolute;
    left: 0;
    top: 129px;
    width: 1200px;
    height: 600px;
    overflow: hidden;
    background: linear-gradient(160deg, var(--royal) 0%, var(--navy) 40%, var(--navy-deep) 100%);
    font-family: "Patua One", Georgia, serif;
    color: var(--white);
  }
  .backdrop {
    position: absolute;
    left: 0;
    top: 0;
    width: 1200px;
    height: 600px;
  }
  .team-photo {
    position: absolute;
    left: 10px;
    top: 120px;
    width: 480px;
    height: 390px;
    border-radius: 200px 200px 0 0;
    background: linear-gradient(180deg, #2b66b0 0%, #6d8fba 38%, #d9e0e8 68%, #f2f4f6 100%);
  }
  .brand {
    position: absolute;
    left: 600px;
    top: 175px;
    display: flex;
    align-items: center;
    gap: 28px;
  }
  .brand-dot {
    width: 110px;
    height: 110px;
    border-radius: 50%;
    background: var(--green);
    flex: none;
  }
  .brand-name {
    line-height: 1;
    color: var(--white);
  }
  .brand-name .primary {
    display: block;
    font-size: 108px;
  }
  .brand-name .secondary {
    display: block;
    font-size: 44px;
    margin-top: 4px;
  }
  .phone {
    position: absolute;
    left: 50px;
    top: 505px;
    font-size: 74px;
    line-height: 1;
    letter-spacing: 1px;
  }
  .website {
    position: absolute;
    left: 650px;
    top: 540px;
    font-size: 38px;
    line-height: 1;
  }
</style>
</head>
<body>
  <div class="billboard">
    <svg class="backdrop" viewBox="0 0 1200 600" aria-hidden="true">
      <path d="M0 0 H120 C220 30 300 120 380 160 C300 150 200 60 0 70 Z" fill="var(--sky-wave)" opacity="0.7"/>
      <path d="M0 495 H560 C590 495 600 530 640 535 H1200 V600 H0 Z" fill="var(--green)"/>
      <path d="M640 535 C608 540 600 585 650 585 H1200 V535 Z" fill="var(--band-blue)"/>
    </svg>

    <div class="team-photo" role="img" aria-label="Photo of the two dentists smiling in white coats in front of the practice"></div>

    <div class="brand">
      <span class="brand-dot"></span>
      <div class="brand-name">
        <span class="primary">Harlow</span>
        <span class="secondary">Family Dentistry</span>
      </div>
    </div>

    <div class="phone">(606) 847-3962</div>
    <div class="website">Harlowfamilydentistry.com</div>
  </div>
</body>
</html>
```